Need brochure designed for my marijuana web startup.

PLEASE READ THE INSTRUCTIONS THOROUGHLY. YOUR SUBMISSION WILL BE REJECTED IF THEY ARE NOT FOLLOWED.

may lead to other immediate design work, such as flyers, postcards, banners, etc.

I need a PRINT trifold brochure or pamphlet designed for my company, Plainleaf.net. We are a bootstrapped medical marijuana search engine, locator, listing service and community.

I will be selling my web product and services to medical marijuana dispensaries and would like to quickly demonstrate why my service is better over my competitors..

I have drafted a (poorly designed) brochure that talks about all the points I wanted to hit on. I'd also like to add our 3 pricing plans in the brochure, but if there isn't any room, i'm fine with that.

I received some design guidelines from a branding consulting firm, so the designs must adhere to those rules. These guidelines are attached as a pdf. These guidelines include things like minimum clear space for the logo, primary and secondary colors, and font style.

Target Market(s)

marijuana dispensaries

Industry/Entity Type

Startup

Font styles to use
Other font styles liked:
• gotham rounded

Colors
9bcb3b

Requirements
Must have
• follow the design guidelines attached, including colors used! font files are attached.
• this is a PRINT brochure request. can be trifold, or 1 fold.
• The TEXT or "COPY" is all included in the brochure.doc attachment. There is additional stats in the "Nice to Haves" section that you may or may not include. up to you. Pricing info is included as an attachment called "Pricing Plan"
• please, keep it simple!
Nice to have
• some graphics.
• pricing plan.
• some statistics that may be interesting to help highlight how special unique items that are hard to find can be easily found with my service:
• From a sample of 2,594 active listings, there are over 153,000 items being sold:
• 12,900 marijuana related accessories (bongs, pipes, clothes, vapor pens, etc.)
• 20,300 concentrates
• 40,400 edibles
• 52,400 flowers (bud and shakes)
• 21,500 other - oral (pills, sprays), topical (lotions, soaps), seeds, oils
• 5,500 pre-rolled marijuana cigarettes (joints, blunts)
• of the 153,000 items, there are:
• 17,750+ hybrid items
• 27,100+ indica items
• 15,000+ sativa items
• in the world of edibles, there are:
• 200+ gluten free items
• 300+ sugar free items
• doses in edibles range from .3mg to 2,353mg (i.e. olive oil) the recommended dosage is 5-10mg
• 2,900+ items of 100mg edibles make it the most common dose offered on the market.
• there are over 4,000 items that are high in CBD (the medicinal chemical of weed).
Should not have
• no photos.

```html
<!DOCTYPE html>
<html lang="en">
<head>
<meta charset="utf-8">
<title>Why plainleaf? – Brochure spread</title>
<link rel="stylesheet" href="https://fonts.googleapis.com/css2?family=Montserrat:wght@300;400;500;600;700&display=swap">
<style>
  :root {
    --backdrop: #d9d9d9;
    --paper: #ffffff;
    --ink: #555659;
    --ink-body: #4a4a4c;
    --brand-green: #8dc63f;
    --leaf-green: #9bcb3b;
    --deep-green: #3a8a3a;
    --navy: #2f5c78;
    --teal: #46a38a;
    --panel: #58595b;
    --panel-text: #ffffff;
  }
  * { margin: 0; padding: 0; box-sizing: border-box; }
  html, body {
    width: 1200px; height: 1000px; overflow: hidden;
    background: var(--backdrop);
    font-family: "Montserrat", "Helvetica Neue", Arial, sans-serif;
    color: var(--ink-body);
  }
  .sheet {
    position: absolute; left: 77px; top: 74px;
    width: 1057px; height: 820px;
    background: var(--paper);
  }
  .abs { position: absolute; }

  .page-title {
    left: 45px; top: 58px;
    font-size: 26px; font-weight: 300; color: var(--ink);
    letter-spacing: 0.2px;
  }
  .column { top: 124px; width: 282px; }
  .column--data { left: 45px; }
  .column--care { left: 393px; }
  .column h2 {
    font-size: 18px; font-weight: 300; color: var(--ink);
    margin-bottom: 18px; white-space: nowrap;
  }
  .column h2 strong { color: var(--brand-green); font-weight: 700; }
  .column p {
    font-size: 11px; line-height: 18.7px; font-weight: 400;
    color: var(--ink-body); margin-bottom: 18.7px;
  }

  .pricing {
    left: 705px; top: 101px; width: 312px; height: 435px;
    background: var(--panel); color: var(--panel-text);
  }
  .pricing h2 {
    position: absolute; left: 35px; top: 22px;
    font-size: 18px; font-weight: 300; white-space: nowrap;
  }
  .pricing h2 strong { color: var(--brand-green); font-weight: 700; }
  .plan { position: absolute; left: 35px; width: 260px; }
  .plan h3 { font-size: 17px; font-weight: 700; color: var(--brand-green); margin-bottom: 6px; }
  .plan ul { list-style: none; }
  .plan li {
    font-size: 8.6px; font-weight: 600; line-height: 13.3px; white-space: nowrap;
  }
  .plan li::before { content: "•"; color: var(--brand-green); margin-right: 4px; }
  .price {
    position: absolute; font-weight: 300; white-space: nowrap; line-height: 1;
  }
  .price .currency { font-size: 20px; vertical-align: top; position: relative; top: 2px; }
  .price .amount { font-size: 50px; letter-spacing: -1px; }
  .price .term { font-size: 8px; font-weight: 400; }
  .plan--starter { top: 68px; }
  .plan--starter .price { left: 133px; top: 26px; }
  .plan--basic { top: 195px; }
  .plan--basic .price { left: 133px; top: 18px; }
  .plan--plus { top: 302px; }
  .plan--plus .price { left: 133px; top: 22px; }

  .timeline { left: 0; top: 0; }
  .stat { position: absolute; width: 140px; }
  .stat .figure { font-size: 18px; font-weight: 500; line-height: 22px; display: block; }
  .stat .label { font-size: 8.6px; line-height: 13.2px; font-weight: 400; display: block; }
  .stat--deep { color: var(--deep-green); }
  .stat--light { color: var(--brand-green); }
  .stat--navy { color: var(--navy); }
  .stat--teal { color: var(--teal); }

  .hub {
    position: absolute; width: 88px; height: 88px;
    display: flex; flex-direction: column; align-items: center; justify-content: center;
    color: #fff; text-align: center;
  }
  .hub .figure { font-size: 17px; font-weight: 600; line-height: 19px; }
  .hub .label { font-size: 8.6px; line-height: 11px; }
</style>
</head>
<body>
<main class="sheet">
  <h1 class="abs page-title">Why plainleaf?</h1>

  <section class="abs column column--data">
    <h2>BIG data + <strong>Marijuana</strong></h2>
    <p>With the ever increasing number of strains, marijuana products and dispensaries flooding the market, it has become increasingly difficult for consumers to find that “one” item.</p>
    <p>The menus offered by most listing services are very limited in the amount of metadata they provide, so searching for a particular strain or item is almost impossible.</p>
    <p>By properly labeling and tagging all the different strains and products with these additional metadata attributes, we have created a powerful search engine to help consumers find very specific items, like Blue Dream Shatter, Grape Ape c02 oil, and even medicated pizzas in their local neighborhood.</p>
  </section>

  <section class="abs column column--care">
    <h2>Compassionate <strong>Care</strong></h2>
    <p>Where would this industry be today if it weren’t for the early pioneers of Compassionate Care? Unfortunately for most services, “compassion” has lost to greed, but we’re here to bring it back!</p>
    <p>We take care of all our plainleaf dispensaries by offering very reasonable prices with no hidden costs and easy to understand plans that have features well beyond our competitors. All of our plans offer a free month trial so you can try before you buy.</p>
    <p>We also don’t accept bribes for favorable search rankings, bigger map markers, or any other unfair features our competitors offer. We believe every dispensary should have a fair chance of success.</p>
  </section>

  <aside class="abs pricing">
    <h2>Pricing <strong>Plan</strong></h2>
    <div class="plan plan--starter">
      <h3>Starter</h3>
      <ul><li>Address</li><li>Contact</li><li>Hours</li><li>Ratings &amp; Reviews</li><li>Member Alerts</li><li>Menu.</li></ul>
      <div class="price"><span class="currency">$</span><span class="amount">19</span><span class="term">/MO</span></div>
    </div>
    <div class="plan plan--basic">
      <h3>Basic</h3>
      <ul><li>Promo Tagline</li><li>Store Description</li><li>Store Features,</li><li>Image Hosting</li><li>Announcements</li></ul>
      <div class="price"><span class="currency">$</span><span class="amount">79</span><span class="term">/MO</span></div>
    </div>
    <div class="plan plan--plus">
      <h3>Plus</h3>
      <ul><li>Daily Dpecials</li><li>First Time Patient Deals</li><li>Search Optimization</li><li>Expanded Item View</li><li>Item Promos</li><li>Advanced Customer Support</li></ul>
      <div class="price"><span class="currency">$</span><span class="amount">349</span><span class="term">/MO</span></div>
    </div>
  </aside>

  <svg class="abs timeline" width="1057" height="820" viewBox="0 0 1057 820" aria-hidden="true">
    <line x1="99" y1="667" x2="957" y2="667" stroke="var(--leaf-green)" stroke-width="1.5"/>
    <circle cx="99" cy="667" r="44" fill="var(--leaf-green)"/>
    <circle cx="957" cy="667" r="44" fill="var(--leaf-green)"/>
    <circle cx="177" cy="667" r="6" fill="var(--deep-green)"/>
    <circle cx="249" cy="667" r="6" fill="var(--brand-green)"/>
    <circle cx="323" cy="667" r="6" fill="var(--navy)"/>
    <circle cx="399" cy="667" r="6" fill="var(--teal)"/>
    <circle cx="478" cy="667" r="6" fill="var(--deep-green)"/>
    <circle cx="560" cy="667" r="6" fill="var(--brand-green)"/>
    <circle cx="635" cy="667" r="6" fill="var(--navy)"/>
    <circle cx="703" cy="667" r="6" fill="var(--teal)"/>
    <circle cx="775" cy="667" r="6" fill="var(--deep-green)"/>
    <circle cx="843" cy="667" r="6" fill="var(--brand-green)"/>
  </svg>

  <div class="hub" style="left:55px; top:623px;"><span class="figure">2,594</span><span class="label">active listings</span></div>
  <div class="hub" style="left:913px; top:623px;"><span class="figure">153,000</span><span class="label">items<br>being sold</span></div>

  <div class="stat stat--deep" style="left:172px; top:571px;"><span class="figure">21,500</span><span class="label">other - oral (pills,<br>sprays), topical<br>(lotions, soaps),<br>seeds, oils</span></div>
  <div class="stat stat--navy" style="left:317px; top:614px;"><span class="figure">40,400</span><span class="label">edibles</span></div>
  <div class="stat stat--deep" style="left:473px; top:571px;"><span class="figure">12,900</span><span class="label">marijuana related<br>accessories<br>(bongs, pipes, clothes,<br>vapor pens, etc.)</span></div>
  <div class="stat stat--navy" style="left:629px; top:585px;"><span class="figure">5,500</span><span class="label">pre-rolled<br>marijuana cigarettes<br>(joints, blunts)</span></div>
  <div class="stat stat--deep" style="left:741px; top:615px;"><span class="figure">27,100+</span><span class="label">indica items</span></div>

  <div class="stat stat--light" style="left:244px; top:686px;"><span class="figure">20,300</span><span class="label">concentrates</span></div>
  <div class="stat stat--teal" style="left:394px; top:686px;"><span class="figure">22,400</span><span class="label">flowers<br>(bud and shakes)</span></div>
  <div class="stat stat--light" style="left:554px; top:686px;"><span class="figure">21,500</span><span class="label">other - oral<br>(pills, sprays),<br>topical (lotions,<br>soaps), seeds, oils</span></div>
  <div class="stat stat--teal" style="left:697px; top:686px;"><span class="figure">17,750+</span><span class="label">hybrid items</span></div>
  <div class="stat stat--light" style="left:836px; top:686px;"><span class="figure">15,000+</span><span class="label">sativa items</span></div>
</main>
</body>
</html>
```